Maple Hollow Bloom Panels Business card

Looking to have a business card design incorporating my logo for my flower wall business.

Industry/Entity Type

Wedding & event planning

Contact Information for Business Card

My business logo, my name - Lena Whitcombe (owner), my tagline - Let us make your day bloom more, phone # 401-726-3148, email address - maplehollowbloompanels@mailvane.net, my website - maplehollowbloompanels.net, Instagram handle- @maplehollowbloompanels, FB handle Handle - maplehollowbloompanels

Font styles to use
Other font styles liked:
• Sentaina is the font that is used in my logo

Requirements
Must have
• Would like a double sided business card

```html
<!DOCTYPE html>
<html lang="en">
<head>
<meta charset="utf-8">
<title>Maple Hollow Bloom Panels – Business Card</title>
<link href="https://fonts.googleapis.com/css2?family=Playfair+Display:wght@400&family=Great+Vibes&family=Roboto:wght@400&display=swap" rel="stylesheet">
<style>
  :root {
    --canvas-bg: #ffffff;
    --card-pink: #fcdfea;
    --card-white: #ffffff;
    --ink: #2b2b2b;
    --ink-soft: #3a3a3a;
    --accent-pink: #d43b98;
    --badge-white: #ffffff;
    --badge-ring: #e3cf9a;
    --shadow: rgba(0, 0, 0, 0.22);
  }
  * { box-sizing: border-box; margin: 0; padding: 0; }
  html, body {
    width: 1200px;
    height: 900px;
    overflow: hidden;
    background: var(--canvas-bg);
  }
  .canvas {
    position: relative;
    width: 1200px;
    height: 900px;
  }
  .card {
    position: absolute;
    top: 290px;
    width: 560px;
    height: 321px;
    box-shadow: 0 14px 38px var(--shadow);
  }
  .card--front { left: 25px; background: var(--card-pink); }
  .card--back  { left: 615px; background: var(--card-white); }

  /* Front side */
  .brand-badge {
    position: absolute;
    left: 190px;
    top: 73px;
    width: 180px;
    height: 180px;
    border-radius: 50%;
    background: var(--badge-white);
    box-shadow: inset 0 0 0 10px var(--badge-white), inset 0 0 0 11px var(--badge-ring);
    display: flex;
    align-items: center;
    justify-content: center;
    text-align: center;
  }
  .brand-name {
    font-family: "Playfair Display", serif;
    font-weight: 400;
    font-size: 22px;
    line-height: 1.2;
    color: var(--ink);
    width: 130px;
  }
  .website {
    position: absolute;
    left: 0;
    right: 0;
    top: 290px;
    text-align: center;
    font-family: "Roboto", sans-serif;
    font-size: 11px;
    letter-spacing: 0.2px;
    color: var(--ink);
  }

  /* Back side */
  .owner-name {
    position: absolute;
    left: 0;
    right: 0;
    top: 82px;
    text-align: center;
    font-family: "Playfair Display", serif;
    font-weight: 400;
    font-size: 44px;
    letter-spacing: -0.5px;
    word-spacing: 8px;
    color: var(--ink);
    line-height: 1;
  }
  .tagline {
    position: absolute;
    left: 0;
    right: 0;
    top: 132px;
    text-align: center;
    font-family: "Great Vibes", cursive;
    font-size: 34px;
    color: var(--accent-pink);
    line-height: 1;
  }
  .contact-col {
    position: absolute;
    top: 238px;
    font-family: "Roboto", sans-serif;
    font-size: 11px;
    color: var(--ink-soft);
    letter-spacing: 0.2px;
  }
  .contact-col--left  { left: 30px; }
  .contact-col--right { left: 308px; }
  .contact-row {
    display: flex;
    align-items: center;
    gap: 8px;
    height: 18px;
  }
  .contact-icon { width: 14px; height: 14px; flex: none; fill: var(--ink); }
  .social-mark {
    width: 13px;
    height: 13px;
    flex: none;
    border: 1.6px solid var(--ink);
    border-radius: 2px;
  }
  .contact-divider {
    position: absolute;
    left: 280px;
    top: 236px;
    width: 1px;
    height: 34px;
    background: var(--accent-pink);
  }
</style>
</head>
<body>
<main class="canvas">

  <section class="card card--front" aria-label="Card front">
    <div class="brand-badge">
      <span class="brand-name">Maple Hollow Bloom Panels</span>
    </div>
    <p class="website">www.maplehollowbloompanels.net</p>
  </section>

  <section class="card card--back" aria-label="Card back">
    <h1 class="owner-name">Lena Whitcombe</h1>
    <p class="tagline">Let us make your day bloom more</p>

    <div class="contact-col contact-col--left">
      <div class="contact-row">
        <svg class="contact-icon" viewBox="0 0 24 24" aria-hidden="true">
          <circle cx="12" cy="12" r="12"/>
          <path d="M8.2 5.8c.5-.3 1.1-.2 1.4.3l1.3 2.1c.3.5.2 1.1-.2 1.4l-.9.7c.6 1.5 1.8 2.8 3.3 3.5l.7-.9c.3-.4 1-.5 1.4-.2l2.1 1.3c.5.3.6.9.3 1.4l-.8 1.2c-.4.6-1.2.9-1.9.7-4-1.1-7.2-4.3-8.3-8.3-.2-.7.1-1.5.7-1.9z" fill="#fff"/>
        </svg>
        <span>401 726 3148</span>
      </div>
      <div class="contact-row">
        <svg class="contact-icon" viewBox="0 0 24 24" aria-hidden="true">
          <path d="M1 5h22v14H1z"/>
          <path d="M1.5 5.5 12 13.5 22.5 5.5" fill="none" stroke="#fff" stroke-width="1.6"/>
        </svg>
        <span>maplehollowbloompanels@mailvane.net</span>
      </div>
    </div>

    <div class="contact-divider" aria-hidden="true"></div>

    <div class="contact-col contact-col--right">
      <div class="contact-row">
        <span class="social-mark" aria-hidden="true"></span>
        <span>handle–@maplehollowbloompanels</span>
      </div>
      <div class="contact-row">
        <span class="social-mark" aria-hidden="true"></span>
        <span>handle Handle– maplehollowbloompanels</span>
      </div>
    </div>
  </section>

</main>
</body>
</html>
```